"Lantern Field" Play - Poster Design for Theatre Group

We are an amateur theatre group based in Geneva, Switzerland. We take pride in eye-catching posters for our shows, which are printed in various sizes.
This design will be for a play in March 2016. The play is called "Lantern Field", and it's a Harwick Medal winner from Marcus Ellery-Pound. The play is about a couple who have everything a family could want, until they lose a child in a life-shattering accident that turns their world upside down. The play charts the couple's bittersweet search to find each other and to find comfort.
Most importantly, we want a design that will make people want to see the show. We don't want to give away the plot or be too heavy-handed about death, but we want it to be clear that it's not a comedy (although there are some lighter moments!).
Attached you will find a template for the poster. This simply has our group name and logo in the top right corner: (Lakeshore Stage Players Circle presents).
You may change the color of both the text and the logo, but please do not change the font, size, or location.
Here is the information that needs to be on the poster, wherever you see fit:
play title: Lantern Field
author byline: by Marcus Ellery-Pound
director line: directed by Rob Feltwick
tagline: How do you keep it together when your whole world's fallen apart?
dates and times:
1-5 March 2016
(Tue-Fri 20:00, Sat 19:00)
location:
Théâtre du Vieux-Moulin
Eaux-Vives, Geneva
websites:
www.lspc.ch
www.scenelettres.ch
Technical Details:
Any font or combination of fonts is acceptable. The largest text should be the play title. The author's name must be at least 50% of the title font size.
For this competition, we would like the version with A3 proportions, which will also be used at F4 (89.5 x 128 cm) and A5 sizes (14.8 x 21 cm). Therefore no text should be below 9pt at A5.
However, from the winning designer we will also need repurposed sizes of the same design. Here is a comprehensive list of the sizes we will need.
1) A3 print poster. Artwork should be 300dpi, CMYK, sent with a 1mm bleed all round, to specification PDF/X-1A:2001. We will need this image in PDF format in addition to the default Artbrigade formats.
2) Chatterly advert picture. 1200px by 628px, RGB jpeg. This must comply with Chatterly’s restrictions on amount of text, which is no more than 20% of area taken up by text.(https://www.chatterly.example/ads/tools/text_overlay).
Because of these restrictions it is sufficient to include just the title and the author's name in this version.
3) Chatterly cover picture: 851px by 314px. RGB jpeg. It is sufficient to include just the title and the author's name in this version.
4) Web banner. 1000px by 300px. RGB jpeg. This version should include just the main image(s), no text.
Theatergoers
Entertainment

```html
<!DOCTYPE html>
<html lang="en">
<head>
<meta charset="utf-8">
<title>Lantern Field – Lakeshore Stage Players Circle</title>
<link rel="stylesheet" href="https://fonts.googleapis.com/css2?family=Open+Sans:ital,wght@0,300;0,400;0,700;1,300;1,400&family=Raleway:wght@200&family=Gochi+Hand&display=swap">
<style>
  :root {
    --bg-light: #8aaec2;
    --bg-mid: #7299b0;
    --bg-dark: #4f7389;
    --ink: #ffffff;
    --ink-soft: #d7e3ea;
    --ink-muted: #c3d4de;
    --figure-light: #b9c3c6;
    --figure-dark: #3a3f42;
  }
  * { margin: 0; padding: 0; box-sizing: border-box; }
  html, body { width: 851px; height: 1200px; overflow: hidden; }
  body { font-family: "Open Sans", Arial, sans-serif; color: var(--ink); }

  .poster {
    position: relative;
    width: 851px;
    height: 1200px;
    overflow: hidden;
    background:
      radial-gradient(ellipse 70% 60% at 50% 45%, var(--bg-light) 0%, var(--bg-mid) 60%, var(--bg-dark) 100%);
  }

  .presenter {
    position: absolute;
    top: 22px;
    right: 34px;
    display: flex;
    align-items: center;
    gap: 16px;
  }
  .presenter-name {
    font-weight: 700;
    font-size: 17px;
    line-height: 22px;
    text-align: right;
    color: var(--ink-soft);
  }
  .presenter-mark {
    width: 96px;
    height: 96px;
    border: 3px solid var(--ink-soft);
    border-radius: 50%;
  }

  .award {
    position: absolute;
    top: 200px;
    left: 0;
    width: 100%;
    text-align: center;
    font-weight: 300;
    font-size: 20px;
    letter-spacing: 0.5px;
    color: var(--ink-muted);
  }

  .key-image {
    position: absolute;
    left: 30px;
    top: 390px;
    width: 700px;
    height: 620px;
  }

  .title {
    position: absolute;
    left: 0;
    top: 225px;
    width: 851px;
    height: 330px;
  }
  .title text {
    font-family: "Raleway", "Helvetica Neue", sans-serif;
    font-weight: 200;
    fill: var(--ink);
  }

  .credits {
    position: absolute;
    left: 330px;
    top: 548px;
    width: 270px;
    text-align: right;
    font-style: italic;
  }
  .credits .author { font-size: 26px; font-weight: 400; }
  .credits .director { font-size: 19px; font-weight: 300; color: var(--ink-soft); margin-top: 2px; }

  .tagline {
    position: absolute;
    left: 432px;
    top: 696px;
    width: 390px;
    font-family: "Gochi Hand", cursive;
    font-size: 31px;
    line-height: 34px;
    transform: rotate(-4deg);
    transform-origin: left top;
  }

  .details {
    position: absolute;
    left: 0;
    top: 975px;
    width: 100%;
    text-align: center;
  }
  .details .dates { font-size: 44px; font-weight: 400; line-height: 54px; }
  .details .times { font-size: 22px; font-weight: 300; color: var(--ink-muted); line-height: 30px; }
  .details .venue { font-size: 34px; font-weight: 400; line-height: 44px; }
  .details .district { font-size: 27px; font-weight: 300; color: var(--ink-muted); line-height: 36px; }

  .websites {
    position: absolute;
    left: 0;
    bottom: 14px;
    width: 100%;
    text-align: center;
    font-style: italic;
    font-weight: 300;
    font-size: 18px;
    color: var(--ink-soft);
    word-spacing: 4px;
  }
</style>
</head>
<body>
<main class="poster">

  <header class="presenter">
    <p class="presenter-name">Lakeshore Stage<br>Players Circle<br>presents</p>
    <span class="presenter-mark" aria-hidden="true"></span>
  </header>

  <p class="award">Winner of the 2007 Harwick Medal for Drama</p>

  <svg class="key-image" viewBox="0 0 700 620" role="img" aria-label="Photograph of a wooden rocking horse hanging upside down, its dark rockers at the top and the pale painted horse dangling below">
    <defs>
      <radialGradient id="figure-tone" cx="50%" cy="45%" r="55%">
        <stop offset="0%" stop-color="var(--figure-light)" stop-opacity="0.75"/>
        <stop offset="100%" stop-color="var(--figure-light)" stop-opacity="0"/>
      </radialGradient>
      <linearGradient id="rocker-tone" x1="0" y1="0" x2="1" y2="0">
        <stop offset="0%" stop-color="var(--figure-dark)" stop-opacity="0"/>
        <stop offset="15%" stop-color="var(--figure-dark)" stop-opacity="0.85"/>
        <stop offset="85%" stop-color="var(--figure-dark)" stop-opacity="0.85"/>
        <stop offset="100%" stop-color="var(--figure-dark)" stop-opacity="0"/>
      </linearGradient>
    </defs>
    <rect x="0" y="0" width="700" height="620" fill="url(#figure-tone)"/>
    <rect x="0" y="20" width="700" height="110" rx="55" fill="url(#rocker-tone)"/>
  </svg>

  <svg class="title" viewBox="0 0 851 330" role="heading" aria-level="1" aria-label="Lantern Field">
    <text x="66" y="142" font-size="190" textLength="688" lengthAdjust="spacingAndGlyphs">LANTERN</text>
    <text x="190" y="318" font-size="190" textLength="554" lengthAdjust="spacingAndGlyphs">FIELD</text>
  </svg>

  <div class="credits">
    <p class="author">by Marcus Ellery-Pound</p>
    <p class="director">directed by Rob Feltwick</p>
  </div>

  <p class="tagline">How do you keep it<br>together when your<br>whole world has<br>fallen apart?</p>

  <section class="details">
    <p class="dates">1st to 5th March 2016</p>
    <p class="times">Tue-Fri 20:00, Sat 19:00</p>
    <p class="venue">Théâtre du Vieux-Moulin</p>
    <p class="district">Eaux-Vives, Geneva</p>
  </section>

  <p class="websites">www.lspc.ch &nbsp; www.scenelettres.ch</p>

</main>
</body>
</html>
```